Business Card,

Keystone Ridge & Holdings LLC (DBA Tallow Dwellings) is a licensed residential contractor in Southwest Louisiana, specializing in custom homes, remodels, additions, and Sheltered Crest roof systems.

We’re looking for a designer who can capture the look and feel of a modern, trustworthy Southern-style builder — a brand that communicates craftsmanship, class, and confidence at a glance.

This design package will be used for client meetings, door-to-door marketing, and online advertising, so we need visuals that stand out both in-hand and on screen.

Target Market(s)

Ages 30–65 Married or family-oriented Household income $85,000+ Own or are purchasing a home and want upgrades, additions, or complete rebuilds Value craftsmanship, reliability, and financing flexibility ($0 down options) Respond well to clear before/after visuals, trust-based branding, and professional presentation 🧠 Design cue: They’re not looking for the cheapest contractor — they want someone they can trust with their home and their money. Designs should look professional, clean, and confident.

Industry/Entity Type

Residential Construction, Custom Home Building & Remodeling

Contact Information for Business Card

Logo, "Tallow Dwellings", “Proudly serving Southwest Louisiana with Quality Craftsmanship & Financing Options”, Full Name + Title Everett Pruitt Licensed Residential Contractor | LA #413962, Financing Options QR Code, Phone :337-529-7830 Email: Everett@tallowdwellings.net, Website: www.keystoneridgebuilders.homes , Service Area: Lake Charles & Surrounding Areas ,“Fully Licensed & Insured” ,A small 5-star icon with “Rated 5 Stars by Local Homeowners” , “Schedule Your Free Design-Build Starter Session Today!”

Font styles to use
Other font styles liked:
• Montserrat Bold for business name, Lora Italic for tagline, open sans regular for contact info,

Colors
0054AA
0677BA
7BADD7
CADEEF
E8F1F8

Requirements
Must have
• (Deep Navy (#1 Color) and Gold or rich metallic accent color) “$0 Down Financing Available” and the QR Code Name, Title, and direct Contact Info, Custom Homes • Additions • Remodels • Sheltered Roofing
Nice to have
• 5 Star Searchly Icon, “Refer a friend — Earn $500 when they build with us.”, Facebook.com/keystoneridgebld
Should not have
• Don’t Cram 10 services, slogans, or contact details. Don’t Mix random colors or fonts to “stand out.”, Don’t Use hammer or roof clip art., Don’t Use script, gothic, or cursive fonts., Don’t Add loud textures or frames.

```html
<!DOCTYPE html>
<html lang="en">
<head>
<meta charset="utf-8">
<title>Tallow Dwellings — Business Card</title>
<link rel="stylesheet" href="https://fonts.googleapis.com/css2?family=Montserrat:wght@500;600;700&family=Caveat+Brush&family=Noto+Serif:wght@600&display=swap">
<style>
  :root {
    --navy: #0f2340;
    --gold: #e3a21a;
    --white: #ffffff;
    --backdrop: #ececec;
  }
  * { box-sizing: border-box; margin: 0; padding: 0; }
  html, body { width: 1200px; height: 800px; overflow: hidden; }
  body {
    background: var(--backdrop);
    position: relative;
    font-family: "Montserrat", Arial, sans-serif;
  }
  .card {
    position: absolute;
    width: 640px;
    height: 385px;
    background: var(--navy);
    border-radius: 30px;
    overflow: hidden;
  }

  /* Front */
  .card-front { left: 59px; top: 52px; }
  .brand-name {
    position: absolute;
    left: 0; right: 0; top: 170px;
    text-align: center;
    font-weight: 700;
    font-size: 47px;
    letter-spacing: 1px;
    color: var(--gold);
    line-height: 1;
  }
  .services {
    position: absolute;
    left: 0; right: 0;
    text-align: center;
    font-family: "Caveat Brush", "Comic Sans MS", cursive;
    color: var(--gold);
    font-size: 25px;
    line-height: 1;
  }
  .services-main { top: 235px; }
  .services-roof { top: 279px; }
  .gold-rule {
    position: absolute;
    left: 0; right: 0; top: 356px;
    height: 4px;
    background: var(--gold);
  }

  /* Back */
  .card-back { left: 496px; top: 370px; height: 386px; }
  .contractor-name {
    position: absolute;
    right: 72px; top: 56px;
    font-weight: 700;
    font-size: 38px;
    letter-spacing: 1.5px;
    color: var(--gold);
    line-height: 1;
  }
  .contractor-title {
    position: absolute;
    right: 85px; top: 103px;
    font-weight: 500;
    font-size: 18px;
    letter-spacing: 0.3px;
    color: var(--white);
  }
  .contact-list { position: absolute; left: 66px; top: 150px; list-style: none; }
  .contact-item {
    display: flex;
    align-items: center;
    color: var(--white);
    font-weight: 600;
    height: 38px;
  }
  .contact-icon { width: 24px; margin-right: 9px; display: flex; justify-content: center; }
  .contact-phone { font-family: "Noto Serif", Georgia, serif; font-size: 25px; }
  .contact-email { font-size: 19px; }
  .contact-web { font-size: 14px; }
  .trust-list { position: absolute; left: 66px; top: 276px; list-style: none; color: var(--white); }
  .trust-item { display: flex; align-items: center; font-size: 18px; font-weight: 600; height: 26px; padding-left: 33px; }
  .trust-item.rating { font-size: 16.5px; padding-left: 0; height: 26px; }
  .trust-item.rating .rating-light { font-weight: 500; margin-left: 5px; }
  .star { width: 24px; margin-right: 9px; display: flex; justify-content: center; }
  .financing-box {
    position: absolute;
    left: 433px; top: 154px;
    width: 139px; height: 134px;
    border: 3px solid var(--gold);
    text-align: center;
  }
  .financing-label {
    margin-top: 13px;
    color: var(--white);
    font-weight: 700;
    font-size: 18px;
    line-height: 23px;
  }
  .financing-code {
    position: absolute;
    left: 24px; top: 68px;
    width: 89px; height: 45px;
    background: var(--white);
    border-radius: 2px;
  }
</style>
</head>
<body>

  <section class="card card-front" aria-label="Business card front">
    <h1 class="brand-name">TALLOW DWELLINGS</h1>
    <p class="services services-main">Custom Homes · Additions · Remodels</p>
    <p class="services services-roof">Sheltered Roofing</p>
    <div class="gold-rule"></div>
  </section>

  <section class="card card-back" aria-label="Business card back">
    <h2 class="contractor-name">EVERETT PRUITT</h2>
    <p class="contractor-title">Licensed Residential Contractor</p>

    <ul class="contact-list">
      <li class="contact-item contact-phone">
        <span class="contact-icon">
          <svg width="20" height="20" viewBox="0 0 24 24" aria-hidden="true"><path fill="#fff" d="M6.6 10.8c1.4 2.8 3.8 5.1 6.6 6.6l2.2-2.2c.3-.3.7-.4 1-.2 1.1.4 2.3.6 3.6.6.6 0 1 .4 1 1V20c0 .6-.4 1-1 1C10.6 21 3 13.4 3 4c0-.6.4-1 1-1h3.5c.6 0 1 .4 1 1 0 1.3.2 2.5.6 3.6.1.3 0 .7-.2 1L6.6 10.8z"/></svg>
        </span>337-529-7830
      </li>
      <li class="contact-item contact-email">
        <span class="contact-icon">
          <svg width="24" height="17" viewBox="0 0 24 17" aria-hidden="true"><rect x="0.5" y="0.5" width="23" height="16" fill="#fff"/><path d="M1 1l11 9 11-9M1 16l8-7M23 16l-8-7" fill="none" stroke="#0f2340" stroke-width="1.4"/></svg>
        </span>Everett@tallowdwellings.net
      </li>
      <li class="contact-item contact-web">
        <span class="contact-icon">
          <svg width="24" height="24" viewBox="0 0 24 24" aria-hidden="true" fill="none" stroke="#fff" stroke-width="1.3"><circle cx="12" cy="12" r="10.5"/><ellipse cx="12" cy="12" rx="4.5" ry="10.5"/><path d="M1.5 12h21M3 6.5h18M3 17.5h18M12 1.5v21"/></svg>
        </span>www.keystoneridgebuilders.homes
      </li>
    </ul>

    <ul class="trust-list">
      <li class="trust-item rating">
        <span class="star">
          <svg width="20" height="19" viewBox="0 0 24 23" aria-hidden="true"><path fill="#e3a21a" d="M12 0l2.9 8.3H24l-7.3 5.3 2.8 8.6L12 17l-7.5 5.2 2.8-8.6L0 8.3h9.1z"/></svg>
        </span>Rated 5 Stars<span class="rating-light">by Local Homeowners</span>
      </li>
      <li class="trust-item">Lake Charles &amp; Surrounding Areas</li>
      <li class="trust-item">Fully Licensed &amp; Insured</li>
    </ul>

    <div class="financing-box">
      <p class="financing-label">FINANCING<br>AVAILABLE</p>
      <svg class="financing-code" viewBox="0 0 89 45" aria-label="Financing options code">
        <rect x="8" y="9" width="27" height="27" fill="#0f2340"/>
        <rect x="15" y="16" width="13" height="13" fill="#fff"/>
        <rect x="54" y="9" width="27" height="27" fill="#0f2340"/>
        <rect x="61" y="16" width="13" height="13" fill="#fff"/>
      </svg>
    </div>
  </section>

</body>
</html>
```